Create print ready logo with business card and stationery

I have a logo created in Photoshop, but I need it vectorized properly so it can be used for print, outdoor signs etc. The logo should be able to scale between 2 cm and at least 3 meters in width. And to be printed using standard printing methods.

I would also want to have your help in creating business cards and stationery. The company is a school so the design for cards and stationery should be simple and NOT be "cute" just because it is a school. Use the logo and colors provided. I would want originals which I could edit names, positions, phone etc in.

I would want originals in jpg, png, eps, ai, psd and pdf with correct color codes (CMYK, RGB etc) so it can be used for both print and on web. I would want ONE separate file per version of the logo. It's actually just two logos and variations of colors. I want the logos both with and without background boxes (black or white).

```html
<!DOCTYPE html>
<html lang="en">
<head>
<meta charset="utf-8">
<title>Lindvik Friskolan Norra – Business Card</title>
<link rel="stylesheet" href="https://fonts.googleapis.com/css2?family=Montserrat:wght@500&family=Open+Sans:wght@400;600&display=swap">
<style>
  :root {
    --page: #e9e6e2;
    --card: #0d0d0d;
    --name-grey: #8f8f8f;
    --text-light: #e6e6e6;
    --accent-red: #d8262f;
    --band-blue: #1d78d6;
    --band-green: #3fae3c;
    --band-purple: #7a3a9c;
    --band-red: #c8282e;
    --band-orange: #f08a1c;
    --band-yellow: #f5dc12;
  }
  * { margin: 0; padding: 0; box-sizing: border-box; }
  html, body { width: 1200px; height: 900px; overflow: hidden; }
  body {
    background: var(--page);
    position: relative;
    font-family: "Open Sans", Arial, sans-serif;
  }
  .card {
    position: absolute;
    width: 620px;
    height: 354px;
    background: var(--card);
    border-radius: 4px;
    box-shadow: 0 10px 26px rgba(0,0,0,.25);
    overflow: hidden;
  }
  .card-front { left: 90px; top: 70px; }
  .card-back  { left: 490px; top: 476px; }

  .front-name {
    position: absolute;
    left: 58px;
    bottom: 58px;
    font-family: "Montserrat", Arial, sans-serif;
    font-weight: 500;
    font-size: 58px;
    line-height: 1.02;
    letter-spacing: 1px;
    text-transform: uppercase;
    color: var(--name-grey);
  }

  .back-name {
    position: absolute;
    left: 40px;
    top: 150px;
    font-family: "Montserrat", Arial, sans-serif;
    font-weight: 500;
    font-size: 30px;
    line-height: 1.1;
    text-transform: uppercase;
    color: var(--name-grey);
  }

  .contact {
    position: absolute;
    left: 360px;
    top: 58px;
    color: var(--text-light);
  }
  .contact-person {
    font-weight: 600;
    font-size: 18px;
    color: var(--accent-red);
    letter-spacing: .5px;
  }
  .contact-title { font-size: 13px; margin-top: 2px; margin-bottom: 18px; }
  .contact-list { list-style: none; font-size: 12.5px; line-height: 1.55; }
  .contact-list li { display: flex; align-items: flex-start; gap: 10px; margin-bottom: 3px; }
  .contact-list svg { flex: none; width: 12px; height: 12px; margin-top: 3px; fill: var(--text-light); }

  .colour-band {
    position: absolute;
    left: 0; right: 0; bottom: 0;
    height: 12px;
    display: flex;
  }
  .colour-band span { flex: 1; }
  .band-blue { background: var(--band-blue); }
  .band-green { background: var(--band-green); }
  .band-purple { background: var(--band-purple); }
  .band-red { background: var(--band-red); }
  .band-orange { background: var(--band-orange); }
  .band-yellow { background: var(--band-yellow); }
</style>
</head>
<body>

<section class="card card-front">
  <p class="front-name">Lindvik<br>Friskolan<br>Norra</p>
</section>

<section class="card card-back">
  <p class="back-name">Lindvik<br>Friskolan<br>Norra</p>

  <div class="contact">
    <p class="contact-person">YOUR NAME</p>
    <p class="contact-title">Title</p>
    <ul class="contact-list">
      <li>
        <svg viewBox="0 0 12 12"><path d="M6 0a4 4 0 0 0-4 4c0 3 4 8 4 8s4-5 4-8a4 4 0 0 0-4-4zm0 5.6A1.6 1.6 0 1 1 6 2.4a1.6 1.6 0 0 1 0 3.2z"/></svg>
        <span>Office: 140 Birch Lane,<br>Harbor Road, Springfield</span>
      </li>
      <li>
        <svg viewBox="0 0 12 12"><path d="M2.4 0.5l2 2.3-1 1.4a7 7 0 0 0 4.4 4.4l1.4-1 2.3 2-1.3 1.9C5.5 11.5.5 6.5.5 1.8z"/></svg>
        <span>(555)-014-0277</span>
      </li>
      <li>
        <svg viewBox="0 0 12 12"><path d="M0 2h12v8H0zm1 1v.4l5 3.2 5-3.2V3z"/></svg>
        <span>info@lindvikfriskolan.example</span>
      </li>
      <li>
        <svg viewBox="0 0 12 12"><circle cx="6" cy="6" r="5.2" fill="none" stroke="#e6e6e6" stroke-width="1.2"/><path d="M.8 6h10.4M6 .8c-2.8 3-2.8 7.4 0 10.4M6 .8c2.8 3 2.8 7.4 0 10.4" fill="none" stroke="#e6e6e6" stroke-width="1"/></svg>
        <span>www.lindvikfriskolan.example</span>
      </li>
    </ul>
  </div>

  <div class="colour-band">
    <span class="band-blue"></span>
    <span class="band-green"></span>
    <span class="band-purple"></span>
    <span class="band-red"></span>
    <span class="band-orange"></span>
    <span class="band-yellow"></span>
  </div>
</section>

</body>
</html>
```